Ultra Modern Smart Home Real Estate Website

We are creating a website to sell our super modern high tech home, I am an ex Creative Director and I am not happy with our realtors design. We need to include a virtual tour which you can view here at www.512MarrowbyCourt.com . The house is being sold furnished and we also have a 3 D model which we want to include you can view here https://my.voxelnest.com/show/?m=tKbwRuvHsLe
The url is www.brisdahouse.com and is hosted on HostNimbo. You can also see our own website at www.brisdagroup.com

Target Market(s)

Buyers that love modern and high technology, I can send a list of all the tech included in the house, my husband is an industry analyst in the computer industry

Industry/Entity Type

Real Estate

Coding

Coded - Design and coding required

Number of Pages Required

1 page

Font styles to use
Sans Serif

Colors
886aae

Requirements
Must have
• The virtual tour, 3 d model, list of tech and showcase of the house and furnishings and a contact form for my realtor
Nice to have
• Purple is my favorite color and we have a few touches in the house so would like to see it as an accent color. Clean simple type and copy, easy to read font, no fancy transitions, less is more design aesthetic.
Should not have
• Complex typography, no ghosted images with type over them that you can't read;-)
• Don't care for the color red

```html
<!DOCTYPE html>
<html lang="en">
<head>
<meta charset="utf-8">
<title>Brisda Group – Ultra Modern Smart Home Real Estate</title>
<link href="https://fonts.googleapis.com/css2?family=Open+Sans:wght@400;600;700;800&display=swap" rel="stylesheet">
<style>
  :root {
    --purple: #886aae;
    --purple-dark: #6f5493;
    --purple-line: #5e477e;
    --field: #8a6bb0;
    --field-border: #b9a3d6;
    --charcoal: #222427;
    --charcoal-2: #1b1d20;
    --black: #050505;
    --coral: #f26f5e;
    --white: #ffffff;
    --muted: #5d6066;
    --ribbon: #f4f4f6;
    --nav-text: #8a6bb0;
  }
  * { box-sizing: border-box; margin: 0; padding: 0; }
  html, body { width: 1001px; height: 1200px; overflow: hidden; background: var(--purple); }
  body { font-family: "Open Sans", Arial, sans-serif; color: var(--white); }
  .page { position: relative; width: 1001px; height: 1200px; overflow: hidden; background: var(--purple); }
  .abs { position: absolute; }

  /* header */
  .site-header { position: absolute; left: 0; top: 0; width: 1001px; height: 86px; background: var(--purple); border-bottom: 2px solid var(--purple-line); }
  .brand { position: absolute; left: 196px; top: 30px; display: flex; align-items: center; gap: 10px; }
  .brand-mark { width: 26px; height: 26px; background: var(--white); }
  .brand-name { font-size: 10px; letter-spacing: 3px; font-weight: 400; color: var(--white); text-transform: uppercase; }
  .main-nav { position: absolute; left: 404px; top: 26px; width: 404px; height: 36px; }
  .main-nav svg { position: absolute; left: 0; top: 0; }
  .main-nav ul { position: absolute; left: 0; top: 0; width: 100%; height: 33px; list-style: none; }
  .main-nav li { position: absolute; top: 0; height: 33px; line-height: 33px; font-size: 8.5px; font-weight: 700; letter-spacing: .6px; color: var(--nav-text); }
  .main-nav li.active { color: #222; background: #e6e6ea; padding: 0 10px; margin-left: -10px; }

  /* gallery */
  .tour-gallery { position: absolute; left: 0; top: 88px; width: 1001px; height: 323px; background: var(--purple); }
  .tour-side, .tour-main { position: absolute; top: 2px; height: 319px; }
  .tour-side { background: linear-gradient(160deg, #d8d8d8, #8b8b8b 55%, #3a3a3a); }
  .tour-side.left { left: 0; width: 189px; }
  .tour-side.right { left: 812px; width: 189px; background: linear-gradient(200deg, #e4e4e4, #9a9a9a 50%, #2f2f2f); }
  .tour-main { left: 196px; width: 610px; background: linear-gradient(180deg, #e9ecef 0%, #cfd3d8 35%, #3a3a44 62%, #2a2628 100%); }
  .tour-address { position: absolute; left: 5px; top: 4px; font-family: Arial, sans-serif; font-size: 13px; color: #e4e6ea; line-height: 16px; }
  .tour-tools { position: absolute; left: 12px; bottom: 6px; display: flex; gap: 12px; }
  .section-rule { position: absolute; left: 0; width: 1001px; height: 2px; background: var(--purple-line); }

  /* welcome */
  .welcome-title { position: absolute; left: 196px; top: 438px; font-size: 21px; line-height: 24px; font-weight: 800; letter-spacing: 1px; }
  .welcome-sub { position: absolute; left: 196px; top: 499px; font-size: 10px; line-height: 16px; font-weight: 700; letter-spacing: 1px; }
  .welcome-rule { position: absolute; left: 196px; top: 545px; width: 32px; height: 2px; background: var(--white); }
  .welcome-text { position: absolute; left: 196px; top: 560px; width: 340px; font-size: 8.3px; line-height: 14.5px; color: #efe9f6; }
  .btn-outline { position: absolute; display: block; border: 1.5px solid var(--white); background: var(--coral); color: var(--white); font-weight: 700; text-align: center; }
  .more-info { left: 196px; top: 635px; width: 68px; height: 24px; line-height: 21px; font-size: 9px; letter-spacing: .5px; }

  /* quick contact */
  .quick-contact { position: absolute; left: 613px; top: 431px; width: 180px; height: 230px; }
  .quick-contact svg { position: absolute; left: 0; top: 0; }
  .qc-title { position: absolute; left: 38px; top: 29px; font-size: 11.5px; font-weight: 700; letter-spacing: .8px; }
  .qc-field { position: absolute; left: 38px; width: 125px; height: 19px; background: var(--field); border: 1px solid var(--field-border); font-size: 7px; color: #fff; padding: 4px 5px; }
  .qc-submit { left: 38px; top: 178px; width: 46px; height: 20px; line-height: 17px; font-size: 7px; letter-spacing: .5px; }

  /* video */
  .video-player { position: absolute; left: 196px; top: 717px; width: 610px; height: 244px; }
  .video-frame { position: absolute; left: 0; top: 0; width: 610px; height: 210px; background: linear-gradient(90deg, #7f9fc9 0%, #c8d7ea 22%, #9fb4d2 45%, #2b3553 62%, #b9cde4 80%, #6e7fb6 100%); }
  .video-controls { position: absolute; left: 0; top: 210px; width: 610px; height: 34px; background: #6f9bc8; border-top: 1px solid #9cbfe2; }
  .press-play { position: absolute; left: 426px; top: 7px; width: 81px; height: 20px; border-radius: 10px; background: #3f6fa6; border: 1px solid #d7e6f5; font-family: Arial, sans-serif; font-size: 10px; line-height: 18px; text-align: center; letter-spacing: .3px; }

  /* showcase */
  .showcase { position: absolute; left: 0; top: 976px; width: 1001px; height: 171px; background: var(--charcoal); }
  .showcase h2 { position: absolute; top: 30px; font-size: 11.5px; font-weight: 700; letter-spacing: .8px; }
  .showcase-thumb { position: absolute; top: 71px; width: 88px; height: 69px; border: 2px solid #3a3c40; background: linear-gradient(180deg, #c9c9c9, #7b7b7b 55%, #d6d6d6); }
  .showcase-text { position: absolute; top: 70px; width: 190px; font-size: 8.2px; line-height: 12.5px; color: var(--muted); }
  .btn-dark { position: absolute; top: 124px; width: 42px; height: 17px; border: 1px solid #4a4c50; background: var(--charcoal-2); font-size: 7.5px; font-weight: 700; line-height: 15px; text-align: center; }

  /* footer */
  .site-footer { position: absolute; left: 0; top: 1147px; width: 1001px; height: 53px; background: var(--black); }
  .copyright { position: absolute; left: 196px; top: 20px; font-size: 7.5px; color: #5a5a5a; }
  .social { position: absolute; top: 18px; width: 17px; height: 17px; border-radius: 50%; }
</style>
</head>
<body>
<div class="page">

  <header class="site-header">
    <div class="brand">
      <span class="brand-mark"></span>
      <span class="brand-name">Brisda Group</span>
    </div>
    <nav class="main-nav">
      <svg width="404" height="36" viewBox="0 0 404 36" aria-hidden="true">
        <polygon points="14,9 0,24 6,33 398,33 404,24 390,9" fill="#cfcfd6"/>
        <polygon points="0,0 404,0 392,16 404,33 0,33 12,16" fill="var(--ribbon)"/>
      </svg>
      <ul>
        <li class="active" style="left:86px">HOME</li>
        <li style="left:140px">ABOUT</li>
        <li style="left:200px">SERVICES</li>
        <li style="left:263px">GALLERY</li>
        <li style="left:327px">CONTACT</li>
      </ul>
    </nav>
  </header>

  <section class="tour-gallery">
    <div class="tour-side left" role="img" aria-label="Black and white view of the master bath with a soaking tub and skylight"></div>
    <div class="tour-main" role="img" aria-label="Virtual tour view of the modern kitchen with dark cabinets and a glass dining table">
      <p class="tour-address">512 Marrowby Court, Calder Vale, CA<br>Floor 2</p>
      <div class="tour-tools">
        <svg width="14" height="18" viewBox="0 0 14 18" aria-label="Walk mode"><circle cx="7" cy="3" r="2" fill="#fff"/><path d="M7 6 L7 11 M7 8 L3 10 M7 8 L11 9 M7 11 L4 16 M7 11 L10 16" stroke="#fff" stroke-width="1.6" fill="none"/><rect x="0" y="17" width="14" height="1" fill="#fff"/></svg>
        <svg width="18" height="18" viewBox="0 0 18 18" aria-label="Model view"><path d="M9 2 L16 6 L16 13 L9 17 L2 13 L2 6 Z M2 6 L9 10 L16 6 M9 10 L9 17" stroke="#fff" stroke-width="1.3" fill="none"/></svg>
        <svg width="18" height="18" viewBox="0 0 18 18" aria-label="Floor plan"><rect x="2" y="2" width="14" height="14" stroke="#fff" stroke-width="1.3" fill="none"/><path d="M2 9 H9 V16 M9 2 V6" stroke="#fff" stroke-width="1.3" fill="none"/></svg>
      </div>
    </div>
    <div class="tour-side right" role="img" aria-label="Black and white view of the dining area with a round glass table"></div>
  </section>
  <div class="section-rule" style="top:413px"></div>

  <section class="welcome">
    <h1 class="welcome-title">WELCOME TO<br>BRISDA GROUP</h1>
    <p class="welcome-sub">ULTRA MODERN SMART<br>HOME REAL ESTATE</p>
    <div class="welcome-rule"></div>
    <p class="welcome-text">Lorem Ipsum is simply dummy text of the printing and typesetting industry. Lorem Ipsum has been the industry's standard dummy text ever since the 1500s. Lorem Ipsum is simply dummy text of the printing and typesetting industry. Lorem Ipsum has been the industry's standard dummy text ever since the 1500s.</p>
    <a class="btn-outline more-info">MORE INFO</a>
  </section>

  <aside class="quick-contact">
    <svg width="180" height="230" viewBox="0 0 180 230" aria-hidden="true">
      <polygon points="0,0 16,14 16,228 2,220" fill="#17181a"/>
      <polygon points="0,0 180,4 180,230 16,230 16,14" fill="var(--charcoal)"/>
    </svg>
    <h3 class="qc-title">QUICK CONTACT</h3>
    <div class="qc-field" style="top:62px">Enter your name...</div>
    <div class="qc-field" style="top:90px">Enter email id...</div>
    <div class="qc-field" style="top:118px;height:40px">Message...</div>
    <a class="btn-outline qc-submit">SUBMIT</a>
  </aside>
  <div class="section-rule" style="top:701px"></div>

  <section class="video-player">
    <div class="video-frame" role="img" aria-label="Panoramic video of the living room with a fireplace, glass shelves and purple glassware">
      <svg style="position:absolute;left:278px;top:82px" width="56" height="56" viewBox="0 0 56 56" aria-hidden="true">
        <circle cx="28" cy="28" r="27" fill="rgba(255,255,255,.45)"/>
        <polygon points="21,15 42,28 21,41" fill="#fff"/>
      </svg>
    </div>
    <div class="video-controls">
      <svg style="position:absolute;left:6px;top:4px" width="26" height="26" viewBox="0 0 26 26" aria-hidden="true">
        <circle cx="13" cy="13" r="12" fill="#3f6fa6" stroke="#d7e6f5"/>
        <polygon points="10,7 19,13 10,19" fill="#fff"/>
      </svg>
      <svg style="position:absolute;left:38px;top:11px" width="380" height="12" viewBox="0 0 380 12" aria-hidden="true">
        <rect x="0" y="2" width="380" height="8" rx="4" fill="#4f7fb3"/>
        <circle cx="6" cy="6" r="5" fill="#e8f0f8"/>
      </svg>
      <span class="press-play">PRESS PLAY</span>
      <svg style="position:absolute;left:513px;top:10px" width="50" height="14" viewBox="0 0 50 14" aria-hidden="true">
        <polygon points="0,5 4,5 9,1 9,13 4,9 0,9" fill="#e8f0f8"/>
        <rect x="14" y="3" width="34" height="8" rx="4" fill="#3f6fa6" stroke="#d7e6f5"/>
        <rect x="22" y="5" width="18" height="4" rx="2" fill="#fff"/>
      </svg>
      <svg style="position:absolute;left:584px;top:3px" width="22" height="22" viewBox="0 0 22 22" aria-hidden="true">
        <rect x="1" y="1" width="20" height="20" rx="3" fill="#3f6fa6" stroke="#d7e6f5"/>
        <rect x="6" y="6" width="10" height="10" fill="#c9dbef"/>
      </svg>
    </div>
  </section>

  <section class="showcase">
    <h2 style="left:199px">TECH AND SHOWCASE</h2>
    <div class="showcase-thumb" style="left:196px" role="img" aria-label="Hallway with marble floor"></div>
    <p class="showcase-text" style="left:299px">Lorem Ipsum is simply dummy text of the printing and typesetting industry. Lorem Ipsum has been the industry's standard dummy text ever since the 1500s.</p>
    <a class="btn-dark" style="left:299px">MORE</a>

    <h2 style="left:508px">HOUSE AND FURNISHINGS</h2>
    <div class="showcase-thumb" style="left:508px" role="img" aria-label="Furnished hallway leading to the living area"></div>
    <p class="showcase-text" style="left:612px">Lorem Ipsum is simply dummy text of the printing and typesetting industry. Lorem Ipsum has been the industry's standard dummy text ever since the 1500s.</p>
    <a class="btn-dark" style="left:612px">MORE</a>
  </section>

  <footer class="site-footer">
    <p class="copyright">Copyright(c) brisdahouse.com</p>
    <span class="social" style="left:708px;background:#3b5998"></span>
    <span class="social" style="left:733px;background:#2aa3e0"></span>
    <span class="social" style="left:759px;background:#dd4b39"></span>
    <span class="social" style="left:784px;background:#1a7bb9"></span>
  </footer>

</div>
</body>
</html>
```